Real State Agency App

We need an app design for a real state agency, we provide mockups for our project that ilustrates very well what we need
our web site is www.brindlevaleestates.com,

Target Market(s)

Tourism

Font styles to use
Other font styles liked:
• attached you will find it

Requirements
Must have
• Colors like the logo

```html
<!DOCTYPE html>
<html lang="en">
<head>
<meta charset="utf-8">
<title>Brindlevale App</title>
<link href="https://fonts.googleapis.com/css2?family=Montserrat:wght@500&family=Open+Sans:wght@400;600;700&family=Kalam:wght@400&display=swap" rel="stylesheet">
<style>
:root{
  --purple-1:#5b2a9e;
  --purple-2:#4a3aa8;
  --purple-3:#3f4fb0;
  --canvas:#e7e6e9;
  --navy:#0b3d8c;
  --ink:#1f2a44;
  --muted:#6b7280;
  --line:#d4d7dd;
  --band:#e2e8f2;
  --sky:#41b0dd;
  --sun:#fdc743;
  --black:#0d0d0d;
  --white:#ffffff;
}
*{box-sizing:border-box;margin:0;padding:0}
html,body{width:1200px;height:2899px;overflow:hidden}
body{background:var(--canvas);font-family:"Open Sans",sans-serif;color:var(--ink);position:relative}
.hero{position:absolute;left:0;top:0;width:1200px;height:470px}
.board-title{position:absolute;top:104px;left:0;width:1200px;text-align:center;font-family:"Montserrat",sans-serif;font-weight:500;font-size:50px;color:var(--white);letter-spacing:1px}
.screen{position:absolute;width:367px;background:var(--white);box-shadow:0 2px 8px rgba(0,0,0,.12);overflow:hidden}
.screen.tall{height:624px}
.screen.short{height:572px}
.status{height:19px;background:var(--black);color:#ddd;font-size:10px;display:flex;align-items:center;justify-content:space-between;padding:0 9px}
.status svg{height:10px;width:48px}
.appbar{height:52px;background:var(--navy);display:flex;align-items:center;justify-content:space-between;padding:0 14px;color:var(--white)}
.appbar svg{width:22px;height:22px}
.appbar h2{font-family:"Kalam",cursive;font-weight:400;font-size:19px;letter-spacing:1.5px}
.abs{position:absolute}
.field{position:absolute;left:41px;width:286px;height:35px;border:1px solid var(--line);font-size:11px;color:#8a8f99;padding:0 13px;display:flex;align-items:center;justify-content:space-between}
.field.area{height:110px;align-items:flex-start;padding-top:12px}
.chev{width:12px;height:8px}
.btn{position:absolute;background:var(--sun);color:var(--ink);font-size:13px;display:flex;align-items:center;justify-content:center;gap:8px}
.band{position:absolute;left:0;top:71px;width:367px;background:var(--band);font-size:11.5px;line-height:19px;text-align:center;color:#333}
.tile{position:absolute;width:155px;height:145px;box-shadow:0 1px 6px rgba(0,0,0,.13);display:flex;flex-direction:column;align-items:center;justify-content:flex-end;padding-bottom:16px;text-align:center;font-size:12px;line-height:17px;color:#333}
.tile svg{width:60px;height:60px;margin-bottom:10px}
.brand{position:absolute;top:84px;left:0;width:367px;display:flex;align-items:center;justify-content:center;gap:10px;color:var(--navy);font-weight:700;font-size:34px}
.brand i{display:block;width:14px;height:14px;border-radius:50%;background:var(--sky)}
.langs{position:absolute;left:21px;top:547px;width:323px;height:32px;display:flex;box-shadow:0 1px 5px rgba(0,0,0,.13)}
.langs span{flex:1;display:flex;align-items:center;justify-content:center;font-size:12px;color:#333}
.langs .on{background:var(--sky);color:var(--white)}
.result{position:absolute;left:17px;width:340px;height:97px;display:flex;gap:11px}
.thumb{width:132px;height:97px;flex:none}
.result h3{font-size:12px;color:var(--navy);font-weight:700;margin:-2px 0 3px}
.result p{font-size:11px;line-height:20px;color:#333}
.result a{font-size:11px;color:var(--sky);text-decoration:underline}
.copy{position:absolute;font-size:12.5px;line-height:19px;color:#555}
.svc{position:absolute;left:42px;width:285px;height:41px;background:var(--sky);color:var(--white);font-size:14px;display:flex;align-items:center;justify-content:center}
.arrow{position:absolute;top:87px;width:28px;height:28px;border-radius:50%;background:rgba(255,255,255,.75);display:flex;align-items:center;justify-content:center}
.arrow svg{width:12px;height:12px}
</style>
</head>
<body>

<svg width="0" height="0" style="position:absolute">
  <defs>
    <symbol id="home" viewBox="0 0 24 24"><path d="M3 11 12 3l9 8M5 9.5V21h5v-6h4v6h5V9.5" fill="none" stroke="#fff" stroke-width="1.8" stroke-linejoin="round"/></symbol>
    <symbol id="search" viewBox="0 0 24 24"><circle cx="10" cy="10" r="6.5" fill="none" stroke="#fff" stroke-width="2.6"/><path d="M15 15l6 6" stroke="#fff" stroke-width="2.8" stroke-linecap="round"/></symbol>
    <symbol id="menu" viewBox="0 0 24 24"><path d="M2 6h20M2 12h20M2 18h20" stroke="#fff" stroke-width="1.8"/></symbol>
    <symbol id="sys" viewBox="0 0 48 10"><path d="M2 9h2V7H2zM5 9h2V5H5zM8 9h2V3H8zM11 9h2V1h-2z" fill="#ccc"/><path d="M20 4.5a7 7 0 0 1 9 0M22 6.5a4 4 0 0 1 5 0" fill="none" stroke="#ccc" stroke-width="1.2"/><circle cx="24.5" cy="8.5" r="1" fill="#ccc"/><rect x="34" y="2" width="11" height="7" rx="1" fill="#ccc"/><rect x="45" y="4" width="1.5" height="3" fill="#ccc"/></symbol>
    <symbol id="chev" viewBox="0 0 12 8"><path d="M1 1.5 6 6l5-4.5" fill="none" stroke="#41b0dd" stroke-width="2"/></symbol>
  </defs>
</svg>

<svg class="hero" viewBox="0 0 1200 470" role="presentation">
  <defs>
    <linearGradient id="heroGrad" x1="0" y1="0" x2="1" y2="0">
      <stop offset="0" stop-color="#5b2a9e"/><stop offset=".6" stop-color="#4a39a8"/><stop offset="1" stop-color="#3d4cae"/>
    </linearGradient>
  </defs>
  <path d="M0 0H1200V460C1000 430 760 430 560 405 360 385 150 370 0 385Z" fill="url(#heroGrad)"/>
  <circle cx="1130" cy="115" r="160" fill="#4f4fb8" opacity=".55"/>
</svg>
<h1 class="board-title">Brindlevale App</h1>

<!-- Home -->
<section class="screen tall" style="left:207px;top:296px">
  <div class="status"><span>9:45</span><svg><use href="#sys"/></svg></div>
  <div class="brand"><i></i>Brindlevale</div>
  <div class="tile" style="left:21px;top:193px">
    <svg viewBox="0 0 60 60" fill="none" stroke="#1b62b3" stroke-width="2"><path d="M6 28 26 10l20 18M11 24v24h18"/><circle cx="38" cy="38" r="9"/><path d="M44.5 44.5 54 54"/><rect x="21" y="26" width="9" height="9"/></svg>
    Search<br>our Properties</div>
  <div class="tile" style="left:189px;top:193px">
    <svg viewBox="0 0 60 60" fill="none" stroke="#1b62b3" stroke-width="2"><circle cx="34" cy="20" r="6"/><path d="M34 6v4M34 30v4M20 20h4M44 20h4M24 10l3 3M41 27l3 3M44 10l-3 3M27 27l-3 3"/><path d="M6 44h10l10 4h14l12-8-3-3-12 5H28M16 40h10"/></svg>
    Our<br>Services</div>
  <div class="tile" style="left:21px;top:350px">
    <svg viewBox="0 0 60 60" fill="none" stroke="#1b62b3" stroke-width="2"><circle cx="24" cy="22" r="7"/><path d="M10 52V42a14 14 0 0 1 28 0v10z"/><path d="M38 14 47 6l9 8v10H38z" /><rect x="44" y="16" width="5" height="8"/></svg>
    Sell your<br>Property with us</div>
  <div class="tile" style="left:189px;top:350px">
    <svg viewBox="0 0 60 60" fill="none" stroke="#1b62b3" stroke-width="2"><path d="M12 8h8l3 10-5 4a24 24 0 0 0 12 12l4-5 10 3v8c0 3-3 5-6 5C22 45 8 30 8 13c0-3 2-5 4-5z"/><rect x="30" y="6" width="24" height="14" rx="2"/><path d="M36 13h1M42 13h1M48 13h1"/><rect x="36" y="36" width="20" height="14"/><path d="M36 36l10 8 10-8"/></svg>
    Contact<br>Us</div>
  <div class="langs"><span>Spain</span><span class="on">English</span><span>German</span></div>
</section>

<!-- Sell -->
<section class="screen tall" style="left:614px;top:296px">
  <div class="status"><span>9:45</span><svg><use href="#sys"/></svg></div>
  <div class="appbar"><svg><use href="#home"/></svg><h2>Sell your Property with us</h2><svg><use href="#search"/></svg></div>
  <div class="band" style="height:95px;padding-top:18px">Lorem Ipsum is simply dummy text of the printing<br>and typesetting industry. Lorem Ipsum<br>has been the industry's standard</div>
  <div class="field" style="top:180px">Name</div>
  <div class="field" style="top:224px">Surname</div>
  <div class="field" style="top:268px">Phone</div>
  <div class="field" style="top:312px">Email</div>
  <div class="field" style="top:357px">Property Name</div>
  <div class="field area" style="top:400px">Property Description</div>
  <div class="btn" style="left:41px;top:525px;width:286px;height:43px">Sell us your property</div>
</section>

<!-- Search -->
<section class="screen tall" style="left:207px;top:949px">
  <div class="status"><span>9:45</span><svg><use href="#sys"/></svg></div>
  <div class="appbar"><svg><use href="#home"/></svg><h2>Search Properties</h2><svg><use href="#search"/></svg></div>
  <div class="field" style="left:39px;top:220px">To Reform<svg class="chev"><use href="#chev"/></svg></div>
  <div class="field" style="left:39px;top:266px">Key</div>
  <div class="field" style="left:39px;top:312px">Type<svg class="chev"><use href="#chev"/></svg></div>
  <div class="field" style="left:39px;top:358px">Area<svg class="chev"><use href="#chev"/></svg></div>
  <div class="btn" style="left:39px;top:410px;width:286px;height:41px"><svg width="14" height="14" viewBox="0 0 24 24"><circle cx="10" cy="10" r="6.5" fill="none" stroke="#1f2a44" stroke-width="3"/><path d="M15 15l6 6" stroke="#1f2a44" stroke-width="3"/></svg>Search Properties</div>
</section>

<!-- Contact -->
<section class="screen tall" style="left:614px;top:949px">
  <div class="status"><span>9:45</span><svg><use href="#sys"/></svg></div>
  <div class="appbar"><svg><use href="#home"/></svg><h2>Contact Us</h2><svg><use href="#search"/></svg></div>
  <div class="field" style="top:153px">Name</div>
  <div class="field" style="top:197px">Surname</div>
  <div class="field" style="top:241px">Phone</div>
  <div class="field" style="top:285px">Email</div>
  <div class="field" style="top:329px">Property<svg class="chev"><use href="#chev"/></svg></div>
  <div class="field area" style="top:375px">Notes</div>
  <div class="btn" style="left:41px;top:500px;width:286px;height:41px">Send us your message</div>
</section>

<!-- Results -->
<section class="screen tall" style="left:207px;top:1602px">
  <div class="status"><span>9:45</span><svg><use href="#sys"/></svg></div>
  <div class="appbar"><svg><use href="#home"/></svg><h2>Search Results</h2><svg><use href="#search"/></svg></div>
  <div class="band" style="height:52px;line-height:52px;font-size:12px"><b>Key:</b> Beach &nbsp;&nbsp; <b>Type:</b> House &nbsp;&nbsp; <b>Area:</b> Palma</div>
  <div class="result" style="top:143px"><div class="thumb" role="img" aria-label="Photo of a villa with a swimming pool" style="background:linear-gradient(180deg,#9cc3e6 0%,#e8d8c4 45%,#3fb2d6 100%)"></div><div><h3>House For sale in Palma</h3><p>Bedrooms: 7<br>Bathrooms: 3<br>Built size: 500 (m²)</p><a>Click Here</a></div></div>
  <div class="result" style="top:263px"><div class="thumb" role="img" aria-label="Photo of a yellow house with a pool" style="background:linear-gradient(180deg,#8fbde0 0%,#d9b560 50%,#4bb0cf 100%)"></div><div><h3>House For sale in Palma</h3><p>Bedrooms: 7<br>Bathrooms: 3<br>Built size: 500 (m²)</p><a>Click Here</a></div></div>
  <div class="result" style="top:384px"><div class="thumb" role="img" aria-label="Photo of a garden pool under pine trees" style="background:linear-gradient(180deg,#4d6a3c 0%,#7c8f5a 50%,#3ab0d0 100%)"></div><div><h3>House For sale in Palma</h3><p>Bedrooms: 7<br>Bathrooms: 3<br>Built size: 500 (m²)</p><a>Click Here</a></div></div>
  <div class="result" style="top:504px"><div class="thumb" role="img" aria-label="Photo of a stone house with garden" style="background:linear-gradient(180deg,#7fb6e4 0%,#c79a6a 55%,#6f8a4a 100%)"></div><div><h3>House For sale in Palma</h3><p>Bedrooms: 7<br>Bathrooms: 3<br>Built size: 500 (m²)</p><a>Click Here</a></div></div>
</section>

<!-- Detail -->
<section class="screen tall" style="left:614px;top:1602px">
  <div class="status"><span>9:45</span><svg><use href="#sys"/></svg></div>
  <div class="appbar"><svg><use href="#home"/></svg><h2>Villa Brindlevale</h2><svg><use href="#menu"/></svg></div>
  <div class="abs" role="img" aria-label="Photo of the villa pool and garden under pine trees" style="left:27px;top:95px;width:319px;height:199px;background:linear-gradient(180deg,#3f5a33 0%,#8a9a6a 45%,#2fb0d4 80%,#5f7a43 100%)">
    <div class="arrow" style="left:6px"><svg viewBox="0 0 12 12"><path d="M8 1 3 6l5 5" fill="none" stroke="#333" stroke-width="2"/></svg></div>
    <div class="arrow" style="right:6px"><svg viewBox="0 0 12 12"><path d="M4 1l5 5-5 5" fill="none" stroke="#333" stroke-width="2"/></svg></div>
  </div>
  <h3 class="abs" style="left:27px;top:310px;font-size:15px;color:var(--navy);font-weight:700">Villa Brindlevale</h3>
  <p class="copy" style="left:27px;top:335px;width:320px">Lorem Ipsum is simply dummy text of the printing and typesetting industry. Lorem Ipsum has been the industry's standard dummy text ever since the 1500s, when an unknown printer.<br><br>galley of type and scrambled it to make a type specimen book. It has survived not only five centuries, but also the leap into electronic typesetting, remaining essentially unchanged.</p>
  <div class="btn" style="left:29px;top:526px;width:284px;height:41px">Send Request Information</div>
</section>

<!-- Services -->
<section class="screen short" style="left:408px;top:2253px">
  <div class="status"><span>9:45</span><svg><use href="#sys"/></svg></div>
  <div class="appbar"><svg><use href="#home"/></svg><h2>Our Services</h2><svg><use href="#search"/></svg></div>
  <p class="copy" style="left:22px;top:97px;width:323px;text-align:center">Lorem Ipsum is simply dummy text of the printing and typesetting industry. Lorem Ipsum has been the industry's standard dummy text ever since the 1500s, when an unknown printer.<br><br>galley of type and scrambled it to make a type specimen book. It has survived not only five centuries, but also the leap into electronic typesetting, remaining essentially unchanged.</p>
  <div class="svc" style="top:300px">Seguros</div>
  <div class="svc" style="top:359px">Compra</div>
  <div class="svc" style="top:418px">Mantenimientos</div>
  <div class="svc" style="top:477px">Obras y Reformas</div>
</section>

</body>
</html>
```